Marlow Realty Real Estate Brokerage Recruiting Flyer

We are a real estate brokerage looking to hire more real estate agents. We need to list everything we have to offer as a company so real estate agents will join our company. this is our company website: www.Marlowrealty.example .

100% COMMISSION NO MONTHLY FEE
$450 Flat Transaction FEE

What We Offer:
24/7 Office Access
Free E & O Insurance for 1st Year
Free Online CE and PLE
Free 1,000 Business Cards
Free Professional Social Media Marketing
Free Printing, Scanning, and Copies
Free Buyer and Seller Presentation Packages
Free Filquay Cloud Based Document Management Access
Access to our Internal Brokerage Forum
Company Profit Sharing!
Private Offices Available to Rent

*Lead Generation Software with over 3,000 Leads
*10 Leads to Start
* Free Personal CRM and Website
*Restrictions and Rules apply

Company Address:
4817 Amberfield Road
Suite 512
Fairfax, VA 22194
Phone: 703-555-0147
email: info@marlowrealty.example

Target Market(s)

Real Estate Agents

Industry/Entity Type

Real Estate

Colors
0555a3
ffffff

Requirements
Must have
• 100% COMMISSION NO MONTHLY FEE
$450 Flat Transaction FEE

What We Offer:
24/7 Office Access
Free Online CE and PLE
Free 1,000 Business Cards
Company Profit Sharing!

*10 Leads to Start

Company Address:
4817 Amberfield Road
Suite 512
Fairfax, VA 22194
Phone: 703-555-0147

```html
<!DOCTYPE html>
<html lang="en">
<head>
<meta charset="utf-8">
<title>Marlow Realty – Agent Recruiting Flyer</title>
<link href="https://fonts.googleapis.com/css2?family=Open+Sans:wght@400;600;700&family=PT+Sans:wght@400;700&display=swap" rel="stylesheet">
<style>
  :root {
    --brand-blue: #0555a3;
    --navy: #1e3f8c;
    --navy-deep: #27226f;
    --ink: #3a3a3a;
    --white: #ffffff;
    --page-bg: #e9e9e9;
    --paper: #fbfbfb;
  }
  * { box-sizing: border-box; margin: 0; padding: 0; }
  html, body { width: 1200px; height: 960px; overflow: hidden; background: var(--page-bg); }
  body { position: relative; font-family: "Open Sans", sans-serif; color: var(--ink); }

  .flyer {
    position: absolute; left: 250px; top: 27px; width: 700px; height: 906px;
    background: linear-gradient(160deg, var(--white) 0%, var(--paper) 55%, #f1f1f1 100%);
    box-shadow: 0 6px 18px rgba(0,0,0,.18);
    overflow: hidden;
  }

  /* Header */
  .brand { position: absolute; left: 68px; top: 38px; display: flex; align-items: center; gap: 10px; }
  .brand-mark { width: 26px; height: 26px; background: var(--navy); }
  .brand-name { font-family: "PT Sans", sans-serif; font-size: 26px; font-weight: 400; color: var(--navy); letter-spacing: .5px; }

  /* Hero */
  .hero { position: absolute; left: 0; top: 95px; width: 700px; height: 215px; }
  .hero-photo { position: absolute; inset: 0;
    background: linear-gradient(180deg, #cfd6dc 0%, #e6e3dc 40%, #8c8478 62%, #3a3633 78%, #9fb0bd 100%); }
  .hero-panel { position: absolute; left: 372px; top: 0; width: 328px; height: 205px;
    background: rgba(30, 63, 140, .88); color: var(--white); padding: 38px 0 0 26px; white-space: nowrap; }
  .hero-commission { font-size: 30px; font-weight: 700; line-height: 1; letter-spacing: -.3px; }
  .hero-fee { font-size: 27px; font-weight: 400; line-height: 1.15; }
  .hero-price { font-size: 31px; font-weight: 700; margin-top: 14px; line-height: 1; }
  .hero-flat { font-size: 26px; font-weight: 400; margin-top: 2px; }

  /* Offer list */
  .offer { position: absolute; left: 145px; top: 326px; width: 520px; }
  .offer-title { font-size: 20px; font-weight: 700; color: var(--navy); letter-spacing: .6px;
    border-bottom: 1.5px solid var(--navy); padding-bottom: 1px; line-height: 26px; }
  .offer-list { list-style: none; margin-top: 4px; }
  .offer-list li { display: flex; align-items: center; font-size: 15px; font-weight: 600; line-height: 18px; color: #4a4a4a; letter-spacing: .3px; white-space: nowrap; }
  .offer-list svg { width: 15px; height: 11px; margin-right: 20px; flex: none; }

  /* Lead band */
  .leads { position: absolute; left: 54px; top: 570px; width: 646px; height: 210px;
    background: linear-gradient(180deg, var(--brand-blue) 0%, var(--navy) 40%, var(--navy-deep) 100%); }
  .leads-photo { position: absolute; left: 14px; top: 22px; width: 300px; height: 188px;
    background: linear-gradient(180deg, #4d7f3c 0%, #b9764f 35%, #e6d3b5 62%, #3f6e2c 85%, #7fa34f 100%); }
  .leads-divider { position: absolute; left: 330px; top: 22px; width: 1.5px; height: 170px; background: var(--white); }
  .leads-list { position: absolute; left: 344px; top: 26px; list-style: none; color: var(--white);
    font-family: "PT Sans", sans-serif; font-size: 17px; line-height: 32px; white-space: nowrap; }
  .leads-list li { display: flex; align-items: center; }
  .leads-list li.cont { padding-left: 24px; }
  .leads-list svg { width: 11px; height: 11px; margin-right: 12px; flex: none; }

  /* Footer */
  .contact { position: absolute; left: 170px; top: 794px; font-family: "PT Sans", sans-serif; font-size: 14px; color: var(--ink); line-height: 18px; font-style: normal; }
  .contact-row { display: flex; align-items: center; white-space: nowrap; }
  .contact-row svg { width: 13px; height: 13px; margin-right: 7px; flex: none; }
  .contact-row.indent { padding-left: 20px; }
  .web { position: absolute; left: 440px; top: 806px; font-family: "PT Sans", sans-serif; white-space: nowrap; }
  .web-url { display: flex; align-items: center; font-size: 15px; font-weight: 700; color: var(--navy); letter-spacing: .4px; }
  .web-url svg { width: 15px; height: 15px; margin-right: 8px; }
  .licensed { font-size: 12.5px; color: var(--ink); margin-top: 10px; margin-left: -30px; }
</style>
</head>
<body>
<main class="flyer">

  <header class="brand">
    <span class="brand-mark"></span>
    <span class="brand-name">Marlow Realty</span>
  </header>

  <section class="hero">
    <div class="hero-photo" role="img" aria-label="Modern white flat-roof house with poolside terrace and lounge chairs"></div>
    <div class="hero-panel">
      <p class="hero-commission">100% COMMISSION</p>
      <p class="hero-fee">NO MONTHLY FEE</p>
      <p class="hero-price">$450</p>
      <p class="hero-flat">Flat Transaction FEE</p>
    </div>
  </section>

  <section class="offer">
    <h2 class="offer-title">WHAT WE OFFER:</h2>
    <ul class="offer-list">
      <li><svg viewBox="0 0 16 12"><path d="M0 6h13M8 1l5 5-5 5" stroke="#1e3f8c" stroke-width="2.4" fill="none"/></svg>24/7 Office Access</li>
      <li><svg viewBox="0 0 16 12"><path d="M0 6h13M8 1l5 5-5 5" stroke="#1e3f8c" stroke-width="2.4" fill="none"/></svg>Free E &amp; O Insurance for 1st Year</li>
      <li><svg viewBox="0 0 16 12"><path d="M0 6h13M8 1l5 5-5 5" stroke="#1e3f8c" stroke-width="2.4" fill="none"/></svg>Free Online CE and PLE</li>
      <li><svg viewBox="0 0 16 12"><path d="M0 6h13M8 1l5 5-5 5" stroke="#1e3f8c" stroke-width="2.4" fill="none"/></svg>Free 1,000 Business Cards</li>
      <li><svg viewBox="0 0 16 12"><path d="M0 6h13M8 1l5 5-5 5" stroke="#1e3f8c" stroke-width="2.4" fill="none"/></svg>Free Professional Social Media Marketing</li>
      <li><svg viewBox="0 0 16 12"><path d="M0 6h13M8 1l5 5-5 5" stroke="#1e3f8c" stroke-width="2.4" fill="none"/></svg>Free Printing, Scanning, and Copies</li>
      <li><svg viewBox="0 0 16 12"><path d="M0 6h13M8 1l5 5-5 5" stroke="#1e3f8c" stroke-width="2.4" fill="none"/></svg>Free Buyer and Seller Presentation Packages</li>
      <li><svg viewBox="0 0 16 12"><path d="M0 6h13M8 1l5 5-5 5" stroke="#1e3f8c" stroke-width="2.4" fill="none"/></svg>Free Filquay Cloud Based Document Management Access</li>
      <li><svg viewBox="0 0 16 12"><path d="M0 6h13M8 1l5 5-5 5" stroke="#1e3f8c" stroke-width="2.4" fill="none"/></svg>Access to our Internal Brokerage Forum</li>
      <li><svg viewBox="0 0 16 12"><path d="M0 6h13M8 1l5 5-5 5" stroke="#1e3f8c" stroke-width="2.4" fill="none"/></svg>Company Profit Sharing!</li>
      <li><svg viewBox="0 0 16 12"><path d="M0 6h13M8 1l5 5-5 5" stroke="#1e3f8c" stroke-width="2.4" fill="none"/></svg>Private Offices Available to Rent</li>
    </ul>
  </section>

  <section class="leads">
    <div class="leads-photo" role="img" aria-label="Cape Cod style house with dormer windows, red front door and green lawn"></div>
    <div class="leads-divider"></div>
    <ul class="leads-list">
      <li><svg viewBox="0 0 12 12"><path d="M6 0v12M0 6h12M1.8 1.8l8.4 8.4M10.2 1.8l-8.4 8.4" stroke="#fff" stroke-width="2"/></svg>Lead Generation Software with over</li>
      <li class="cont">3,000 Leads</li>
      <li><svg viewBox="0 0 12 12"><path d="M6 0v12M0 6h12M1.8 1.8l8.4 8.4M10.2 1.8l-8.4 8.4" stroke="#fff" stroke-width="2"/></svg>10 Leads to Start</li>
      <li><svg viewBox="0 0 12 12"><path d="M6 0v12M0 6h12M1.8 1.8l8.4 8.4M10.2 1.8l-8.4 8.4" stroke="#fff" stroke-width="2"/></svg>Free Personal CRM and Website</li>
      <li><svg viewBox="0 0 12 12"><path d="M6 0v12M0 6h12M1.8 1.8l8.4 8.4M10.2 1.8l-8.4 8.4" stroke="#fff" stroke-width="2"/></svg>Restrictions and Rules apply</li>
    </ul>
  </section>

  <footer>
    <address class="contact">
      <div class="contact-row"><svg viewBox="0 0 12 14"><path d="M6 0C2.7 0 0 2.6 0 5.8 0 10 6 14 6 14s6-4 6-8.2C12 2.6 9.3 0 6 0z" fill="#1e3f8c"/><circle cx="6" cy="5.6" r="2.1" fill="#fff"/></svg>4817 Amberfield Road, Suite 512</div>
      <div class="contact-row indent">Fairfax, VA 22194</div>
      <div class="contact-row"><svg viewBox="0 0 14 14"><path d="M3 0.8l2.2 3-1.3 1.6c.8 1.8 2 3 3.7 3.8l1.6-1.3 3 2.2-1.2 2.6C6 12.3 1.6 8 .5 2z" fill="#1e3f8c"/></svg>Phone: 703-555-0147</div>
      <div class="contact-row"><svg viewBox="0 0 14 10"><rect x="0.5" y="0.5" width="13" height="9" fill="#1e3f8c"/><path d="M0.5 0.8l6.5 5 6.5-5" stroke="#fff" fill="none"/></svg>email: info@marlowrealty.example</div>
    </address>
    <div class="web">
      <div class="web-url"><svg viewBox="0 0 16 16"><circle cx="8" cy="8" r="7" fill="none" stroke="#1e3f8c" stroke-width="1.6"/><ellipse cx="8" cy="8" rx="3" ry="7" fill="none" stroke="#1e3f8c" stroke-width="1.3"/><path d="M1 8h14M2.2 4.5h11.6M2.2 11.5h11.6" stroke="#1e3f8c" stroke-width="1.2"/></svg>WWW.MARLOWREALTY.EXAMPLE</div>
      <p class="licensed">Licensed in D.C., Maryland, and Virginia</p>
    </div>
  </footer>

</main>
</body>
</html>
```